Updated Business Card for Optometry Practice

We're a growing optometry practice that is moving to a beautiful new office and we want to update our business card. We just updated our logo so the new card should reflect the new logo. Our practice continually invests in state of the art instruments to help us provide eye care that is thorough, comfortable, efficient and educational.

I've attached our current card and logo. You can reference this for the information I would like on the card. The tag line on the back is "Clearer vision starts right here."

Upon completion of this project we will need (amongst other formats) Photoshop files of the card so I can change employee names to print cards for each employee.

```html
<!DOCTYPE html>
<html lang="en">
<head>
<meta charset="utf-8">
<title>Brightwell Family Eyecare – Business Card</title>
<link href="https://fonts.googleapis.com/css2?family=Montserrat:wght@400;500;600;700&display=swap" rel="stylesheet">
<style>
  :root {
    --navy: #1b2a4f;
    --navy-soft: #22335c;
    --gold: #cfa832;
    --white: #ffffff;
    --ink: #1b2a4f;
    --backdrop: #ebebeb;
  }
  * { box-sizing: border-box; margin: 0; padding: 0; }
  html, body {
    width: 1200px; height: 901px; overflow: hidden;
    background: var(--backdrop);
    font-family: "Montserrat", sans-serif;
  }
  .stage { position: relative; width: 1200px; height: 901px; }
  .card {
    position: absolute;
    width: 560px; height: 320px;
    box-shadow: 0 6px 18px rgba(0,0,0,0.12);
    overflow: hidden;
  }
  /* back side */
  .card-back { left: 170px; top: 70px; background: var(--navy); }
  .card-back .pattern {
    position: absolute; inset: 0;
    background: radial-gradient(circle at 50% 45%, var(--navy-soft), var(--navy) 70%);
  }
  .brand {
    display: flex; align-items: center; gap: 14px;
    white-space: nowrap;
  }
  .card-back .brand {
    position: absolute; left: 0; right: 0; top: 110px;
    justify-content: center; color: var(--white);
  }
  .brand-dot { width: 22px; height: 22px; border-radius: 50%; background: var(--gold); flex: none; }
  .brand-name { font-weight: 600; font-size: 30px; letter-spacing: 0.5px; }
  .tagline {
    position: absolute; left: 0; right: 0; top: 230px;
    text-align: center; color: var(--gold);
    font-weight: 700; font-size: 17px;
  }
  /* front side */
  .card-front { left: 470px; top: 500px; background: var(--white); }
  .card-front .brand {
    position: absolute; left: 36px; top: 40px; gap: 12px; color: var(--navy);
  }
  .card-front .brand-name { font-size: 26px; }
  .person { position: absolute; left: 40px; top: 150px; }
  .person-name { font-weight: 700; font-size: 21px; color: var(--ink); }
  .person-role { font-weight: 500; font-size: 15px; color: var(--gold); margin-top: 2px; }
  .contacts { position: absolute; left: 40px; top: 222px; list-style: none; }
  .contacts li {
    display: flex; align-items: center; gap: 10px;
    font-size: 14px; color: var(--ink); line-height: 26px; white-space: nowrap;
  }
  .contacts svg { width: 16px; height: 16px; flex: none; }
  .address {
    position: absolute; right: 34px; top: 176px;
    text-align: right; font-size: 14px; font-style: normal;
    color: var(--ink); line-height: 21px; white-space: nowrap;
  }
  .address .practice { color: var(--gold); font-weight: 600; }
</style>
</head>
<body>
<main class="stage">
  <section class="card card-back" aria-label="Card back">
    <div class="pattern" role="img" aria-label="Subtle repeating motif on navy background"></div>
    <div class="brand">
      <span class="brand-dot"></span>
      <span class="brand-name">Brightwell Family Eyecare</span>
    </div>
    <p class="tagline">Clearer vision starts right here.</p>
  </section>

  <section class="card card-front" aria-label="Card front">
    <div class="brand">
      <span class="brand-dot"></span>
      <span class="brand-name">Brightwell Family Eyecare</span>
    </div>

    <div class="person">
      <p class="person-name">Daniel Marsh, OD</p>
      <p class="person-role">Optometrist</p>
    </div>

    <ul class="contacts">
      <li>
        <svg viewBox="0 0 16 16" aria-hidden="true"><path fill="var(--gold)" d="M3.5 1.5l2.5 0 1 3.5-1.7 1.2a8 8 0 0 0 4.5 4.5L11 9l3.5 1v2.5c0 1-1 2-2 2C6.5 14.5 1.5 9.5 1.5 3.5c0-1 1-2 2-2z"/></svg>
        (555) 014-2290
      </li>
      <li>
        <svg viewBox="0 0 16 16" aria-hidden="true"><rect x="1" y="3" width="14" height="10" rx="1" fill="var(--gold)"/><path d="M1.5 3.5L8 9l6.5-5.5" fill="none" stroke="#fff" stroke-width="1.3"/></svg>
        dan@brightwelleyecare.com
      </li>
      <li>
        <svg viewBox="0 0 16 16" aria-hidden="true"><g fill="none" stroke="var(--gold)" stroke-width="1.2"><circle cx="8" cy="8" r="6.5"/><ellipse cx="8" cy="8" rx="3" ry="6.5"/><path d="M1.5 8h13M2.5 4.8h11M2.5 11.2h11"/></g></svg>
        www.brightwelleyecare.com
      </li>
    </ul>

    <address class="address">
      <span class="practice">Brightwell Family Eyecare</span><br>
      2750 Linden Crossing Blvd #210<br>
      Brightwell, MO 63000
    </address>
  </section>
</main>
</body>
</html>
```